Foster/Adoptive Family Ministry needs a postcard design to highlight changed lives

Kin Harbor is a non profit that finds and supports foster and adoptive families for kids in need. We need a postcard design that features families and children who have experienced a changed life by working with Kin Harbor. I'm thinking of a postcard that is custom size...so that it fits in a #10 envelope. So that 3 cards could be printed on an 8 1/2 x 11 card stock. The card should be front and back with a layout for a couple of photos, our logo, a headline and some text that will tell the story of the family. This is all about telling a story. The primary audience for the card is donors, and prospective donors. I don't have photos or the text yet, so I'm looking for an editable layout where I can drop text and photos in.

Industry/Entity Type

Non Profit

```html
<!DOCTYPE html>
<html lang="en">
<head>
<meta charset="utf-8">
<title>Kin Harbor Postcard</title>
<link rel="stylesheet" href="https://fonts.googleapis.com/css2?family=Aldrich&family=Open+Sans:wght@400;600&display=swap">
<style>
  :root {
    --page-bg: #e4e4e4;
    --card-bg: #ffffff;
    --brand-blue: #2a7fc4;
    --brand-navy: #1d2a44;
    --ink-grey: #3a3a3a;
    --body-ink: #1e1e1e;
    --band-blue: #2b7cc1;
    --photo-warm-a: #c9a58f;
    --photo-warm-b: #7d6a5c;
    --photo-cool-a: #8aa3c4;
    --photo-cool-b: #2f5f9a;
  }
  * { margin: 0; padding: 0; box-sizing: border-box; }
  html, body { width: 1200px; height: 1068px; overflow: hidden; }
  body { background: var(--page-bg); position: relative; font-family: "Open Sans", Arial, sans-serif; }

  .postcard { position: absolute; left: 36px; width: 1128px; background: var(--card-bg); overflow: hidden; }
  .postcard--front { top: 32px; height: 479px; }
  .postcard--back { top: 543px; height: 485px; }

  .family-photo { position: absolute; }
  .postcard--front .family-photo {
    left: 0; top: 0; width: 1128px; height: 356px;
    background: linear-gradient(100deg, var(--photo-warm-a) 0%, #a88470 35%, var(--photo-warm-b) 70%, #4a3a33 100%);
  }

  .headline-tech { font-family: "Aldrich", sans-serif; font-weight: 400; color: var(--brand-blue); }

  .front-tagline { position: absolute; left: 40px; top: 378px; font-size: 27.5px; white-space: nowrap; letter-spacing: 0.2px; }
  .front-call { position: absolute; left: 40px; top: 426px; font-size: 30px; color: var(--ink-grey); white-space: nowrap; }
  .front-call .call-label { margin-right: 20px; }

  .brand-mark { position: absolute; display: flex; align-items: center; gap: 10px; }
  .brand-mark .brand-dot { width: 22px; height: 22px; border-radius: 50%; background: var(--brand-blue); }
  .brand-mark .brand-name { font-family: "Open Sans", Arial, sans-serif; font-weight: 600; font-size: 31px; color: var(--brand-navy); letter-spacing: -0.5px; }
  .postcard--front .brand-mark { left: 918px; top: 420px; }
  .postcard--back .brand-mark { left: 912px; top: 68px; }

  .postcard--back .family-photo {
    left: 14px; top: 27px; width: 520px; height: 376px;
    border-radius: 120px 120px 0 0;
    background: linear-gradient(180deg, var(--photo-cool-a) 0%, var(--photo-cool-b) 100%);
  }
  .contact-band { position: absolute; left: 0; top: 403px; width: 1128px; height: 82px; background: var(--band-blue); }
  .back-headline { position: absolute; right: 37px; top: 180px; text-align: right; font-size: 35px; line-height: 44px; white-space: nowrap; }
  .back-story { position: absolute; right: 37px; top: 284px; width: 445px; text-align: right; font-size: 17.5px; line-height: 30px; color: var(--body-ink); }
  .site-url { position: absolute; right: 40px; top: 430px; font-family: "Aldrich", sans-serif; font-size: 23px; color: #ffffff; letter-spacing: 0.5px; }
</style>
</head>
<body>
  <section class="postcard postcard--front">
    <div class="family-photo" role="img" aria-label="Group photo of smiling foster and adoptive families with their children"></div>
    <p class="front-tagline headline-tech">Henda velendi tatiscia quibusandion coreped issimus</p>
    <p class="front-call headline-tech"><span class="call-label">Call Today!</span>555-014-2297</p>
    <div class="brand-mark"><span class="brand-dot"></span><span class="brand-name">Kin Harbor</span></div>
  </section>

  <section class="postcard postcard--back">
    <div class="contact-band"></div>
    <div class="family-photo" role="img" aria-label="Cut-out photo of a laughing family, parents giving their children piggyback rides"></div>
    <div class="brand-mark"><span class="brand-dot"></span><span class="brand-name">Kin Harbor</span></div>
    <h2 class="back-headline headline-tech">Santiusd anducit atiorum<br>nosaese quiatus atem consed</h2>
    <p class="back-story">Loriam, opta dicid endelic tota non et magni tem. Nemporem cum aut utaerum quasitatur aliqui quia dolor autest, sunt volorporem assi.</p>
    <p class="site-url">www.kinharbor.org</p>
  </section>
</body>
</html>
```